Website Redesign for a Restaurant with International Cuisine

We need a new website design for a Czech restaurant website that should be modern, simple, flexible, and mobile-friendly. We only need the PSD's, not the website coded.

-- Available images
https://files.veltrobox.com/share/9QxTmr4LpZ7wKd2NaY3bHc8Ve5

-- Our current website
https://beta.ohnivakorna.cz

-- Website we like
https://www.elpatiomorado.cz/en/
https://www.bellhavenhall.com/

## Design following pages of our current website with given effort distribution:
-- 40% Home page, https://www.ohnivakorna.cz/
-- 30% Regular Menu, https://www.ohnivakorna.cz/stala_nabidka
-- 20% Contacts, https://www.ohnivakorna.cz/kontakty
-- 10% About Us, https://www.ohnivakorna.cz/o_nas

## Our strengths
-- Cozy, clean environment
-- we use USDA Prime and USDA Choice class meat
-- helpful, friendly staff
-- high quality traditional international cuisine (that is rare)
-- unique wood-fired oven
-- open parking space

## Our weaknesses
-- longer wait times (especially on weekends)
-- slightly expensive prices

Target Market(s)

People interested in gastronomy looking for high quality dishes.

Industry/Entity Type

Restaurant

Number of Pages Required

4 page

Font styles to use
Serif
Sans Serif

Colors

Designer to choose colors to be used in the design.

Requirements
Must have
• -- Preserve current content structure and the order of indiviual elements (use https://www.ohnivakorna.cz).
• -- Emphasize both weekend events and daily deals. Weekend events are more of a priority.
• -- Also emphasize logo and the restaurant owner’s profile and the link to Google Maps.
• -- Mobile-friendly
• -- Use photos from our gallery to maximize authenticity:
• https://files.veltrobox.com/share/9QxTmr4LpZ7wKd2NaY3bHc8Ve5
Nice to have
• -- Solutions with higher accessibility compliance (WCAG) are preferred.
• -- You may add important links/buttons or rephrase them if necessary.
Should not have
• -- Do not use photos from the current website. You may use externally sourced images if necessary.
• -- Do not use endless animations (carousels).
• -- Do not use embedded content (e.g. interactive map). You may or may not use a map as background decoration for that section.
• -- Nothing too crowded / busy.
• -- Not too many colors.

```html
<!DOCTYPE html>
<html lang="en">
<head>
<meta charset="utf-8">
<title>Ohnivá Korna – A Fusion Restaurant</title>
<link rel="stylesheet" href="https://fonts.googleapis.com/css2?family=Roboto+Slab:wght@300;400;700;800&family=Roboto:wght@300;400;500&display=swap">
<style>
:root{
  --red:#c5161d;
  --red-dark:#9e1016;
  --gold:#f0c232;
  --gold-soft:#e9b92a;
  --dark:#2a2a2a;
  --darker:#1f1f1f;
  --panel:#3a3a3a;
  --light:#ececec;
  --card:#dcdcdc;
  --ink:#2b2b2b;
  --muted:#8a8a8a;
  --white:#ffffff;
}
*{box-sizing:border-box;margin:0;padding:0}
html,body{width:1200px;height:3226px;overflow:hidden}
body{background:var(--dark);font-family:"Roboto",Arial,sans-serif;color:var(--white);position:relative}
.abs{position:absolute}
a{text-decoration:none}

/* header + hero */
.hero{position:absolute;left:0;top:0;width:1200px;height:505px;
  background:radial-gradient(ellipse at 70% 30%,#5a3a2c 0%,#3a2a22 35%,#1d1a18 75%),#1d1a18}
.hero-shade{position:absolute;inset:0;background:linear-gradient(180deg,rgba(0,0,0,.45) 0,rgba(0,0,0,0) 30%,rgba(0,0,0,.35) 100%)}
.site-name{left:157px;top:26px;font-size:16px;color:var(--gold);letter-spacing:.5px;text-transform:uppercase}
.nav{right:148px;top:26px;display:flex;gap:34px;font-size:15px;color:var(--gold);text-transform:uppercase}
.nav .current{color:var(--white);position:relative}
.nav .current::after{content:"";position:absolute;left:0;right:0;bottom:-9px;height:3px;background:var(--red)}
.logo{left:482px;top:0;width:174px;height:161px;background:var(--red);display:flex;flex-direction:column;align-items:center;justify-content:center;gap:12px}
.logo-dot{width:54px;height:54px;border-radius:50%;background:var(--gold)}
.logo-name{font-family:"Roboto Slab",Georgia,serif;font-weight:700;font-size:22px;line-height:26px;color:var(--white);text-align:center}
.hero-title{left:0;width:1200px;top:248px;text-align:center;font-family:"Roboto Slab",Georgia,serif;font-weight:700;font-size:38px;letter-spacing:4px;color:var(--gold)}
.hero-rule{left:570px;top:302px;width:60px;height:4px;background:var(--red)}
.hero-text{left:330px;width:540px;top:318px;text-align:center;font-size:14px;line-height:27px;color:#eee;font-weight:300}

/* chef */
.chef{position:absolute;left:0;top:505px;width:1200px;height:387px;background:var(--dark)}
.chef-name{left:157px;top:68px;font-family:"Roboto Slab",Georgia,serif;font-weight:400;font-size:18px;color:var(--red)}
.chef-name span{font-family:"Roboto",Arial,sans-serif;font-weight:400;font-size:14px;color:#ccc}
.chef-bio{left:157px;top:126px;font-size:13px;line-height:23px;color:#9a9a9a;font-weight:300}
.chef-photo{left:630px;top:48px;width:413px;height:300px;border:2px solid #888;background:linear-gradient(160deg,#5b3a24 0%,#7a5a3a 40%,#d9d5cf 75%,#eae7e2 100%)}

/* quick links */
.quick{position:absolute;left:0;top:892px;width:1200px;height:80px;background:var(--darker)}
.btn{position:absolute;height:45px;border:2px solid var(--gold);color:var(--white);font-size:14px;display:flex;align-items:center;justify-content:center;background:transparent}
.btn.active{border-color:var(--red);font-size:16px;border-radius:4px}
.btn.on-light{color:var(--ink);height:34px;font-size:13px}

/* about */
.about{position:absolute;left:0;top:972px;width:1200px;height:468px;background:var(--light);color:var(--ink)}
.section-title{position:absolute;left:0;width:1200px;text-align:center;font-family:"Roboto Slab",Georgia,serif;font-weight:800;font-size:30px;letter-spacing:1.5px}
.section-rule{position:absolute;left:570px;width:60px;height:5px;background:var(--red)}
.team-photo{left:161px;top:107px;width:456px;height:254px;border:2px solid #fff;background:linear-gradient(180deg,#b4232a 0%,#c9534f 35%,#efe8e4 70%,#d8d4d0 100%)}
.about-text{left:636px;top:110px;width:410px;font-size:14px;line-height:24px;color:#333}
.interior-photo{left:578px;top:301px;width:465px;height:167px;background:radial-gradient(ellipse at 40% 30%,#c8262b 0%,#9b1d21 40%,#3d2c2a 100%);z-index:2}

/* menu */
.menu{position:absolute;left:0;top:1440px;width:1200px;height:1209px;background:var(--dark)}
.menu .section-title{color:var(--white)}
.tagline{left:0;width:1200px;top:140px;text-align:center;font-size:24px;line-height:26px;color:var(--white);font-weight:300}
.tagline em{font-style:normal;color:var(--gold)}
.menu-sub{left:0;width:1200px;top:198px;text-align:center;font-size:13px;color:var(--gold)}
.menu-quote{left:0;width:1200px;top:234px;text-align:center;font-size:13px;line-height:22px;color:var(--gold-soft)}
.menu-quote small{display:block;color:var(--red);font-size:12px}
.card{left:204px;top:306px;width:794px;height:759px;background:linear-gradient(180deg,#e2e2e2,#d4d4d4)}
.card h3{position:absolute;font-family:"Roboto Slab",Georgia,serif;font-weight:700;font-size:28px;color:var(--ink)}
.card .rule{position:absolute;width:36px;height:4px;background:var(--red)}
.card .meta{position:absolute;font-size:13px;line-height:20px;color:#777}
.card .meta b{font-weight:400;color:var(--red)}
.card .desc{position:absolute;font-size:13.5px;line-height:19px;color:#333}
.dish{position:absolute;text-align:center;color:var(--ink)}
.dish .icon{margin:0 auto;width:90px;height:90px;border-radius:50%;background:#fff;border:3px solid #cfcfcf;display:flex;align-items:center;justify-content:center}
.dish h4{font-family:"Roboto Slab",Georgia,serif;font-weight:700;font-size:17px;margin-top:16px}
.dish p{font-size:13px;line-height:19px;margin-top:14px}
.dish .note{font-size:12px;color:#888;margin-top:6px;line-height:19px}
.dish .price{font-size:13px;color:var(--red);margin-top:2px;line-height:19px}
.vline{position:absolute;width:1px;background:#a8a8a8}
.menu-links{left:157px;top:1101px;width:890px;height:75px;background:#4a4a4a}
.menu-links .btn{height:46px;top:14px}

/* contact */
.contact{position:absolute;left:0;top:2649px;width:1200px;height:346px;background:#cfd6dc;color:var(--ink)}
.contact-side{position:absolute;top:0;height:346px;background:linear-gradient(180deg,#c7d3de,#d9dde0 60%,#c4c8c2)}
.contact-side::after{content:"";position:absolute;inset:0;background:rgba(255,255,255,.55)}
.contact-photo{left:383px;top:0;width:436px;height:346px;background:linear-gradient(180deg,#8fb3d6 0%,#bcd2e6 38%,#e6e2dc 55%,#7c8d5a 85%,#5c6b3e 100%)}
.contact .section-title{width:436px;left:383px;top:16px;font-size:28px}
.contact-block{position:absolute;top:90px;font-size:14px;line-height:23px;z-index:2}
.contact-block h5{font-family:"Roboto Slab",Georgia,serif;font-weight:700;font-size:17px;margin-bottom:6px}
.map-btn{left:524px;top:286px;width:162px;height:36px;background:var(--red);color:#fff;font-size:14px;display:flex;align-items:center;justify-content:center}

/* footer */
.footer{position:absolute;left:0;top:2995px;width:1200px;height:231px;background:var(--darker);color:#ddd}
.foot-nav{left:0;width:1200px;top:32px;display:flex;justify-content:center;gap:58px;font-size:13px;color:#fff}
.foot-book{left:0;width:1200px;top:70px;text-align:center;font-size:13px}
.foot-book b{font-weight:400;color:var(--red)}
.social{left:0;width:1200px;top:110px;display:flex;justify-content:center;gap:60px;font-size:13px}
.social div{display:flex;flex-direction:column;align-items:center;gap:6px;width:86px}
.social i{width:14px;height:14px;border-radius:50%;border:2px solid #bbb;display:block}
.social .cur{color:#4a7bd0}
.social .cur i{border-color:#4a7bd0}
.foot-meta{left:0;width:1200px;top:196px;display:flex;justify-content:center;gap:60px;font-size:12px;color:#777}
</style>
</head>
<body>

<header class="hero">
  <div class="hero-shade" role="img" aria-label="Close-up of a grilled steak on a dark wooden board with peppercorns and coarse salt"></div>
  <div class="abs site-name">Restaurant Ohnivá Korna</div>
  <nav class="abs nav"><span>About us</span><span class="current">Menu</span><span>Contact</span></nav>
  <div class="abs logo"><div class="logo-dot"></div><div class="logo-name">OHNIVÁ<br>KORNA</div></div>
  <h1 class="abs hero-title">A FUSION RESTAURANT</h1>
  <div class="abs hero-rule"></div>
  <p class="abs hero-text">Preparing fantastic, popular, international dishes by authentic traditional means. Our recipes always include only fresh ingredients and the greatest regard for original ways of preparation.</p>
</header>

<section class="chef">
  <h2 class="abs chef-name">Tomáš Veverka, <span>Owner and Chef</span></h2>
  <p class="abs chef-bio">A recognized Grilling and Broiling Expert<br>Member and certified commissioner of CGA (Czech),<br>member of HRA (Czech) and its gastronomy section.<br>Restaurateur of the Year 2007 and nominated in 2018 (Czech).<br>Winner of the Bronze Medal of the Culinary Guild (Czech).</p>
  <div class="abs chef-photo" role="img" aria-label="Portrait of the owner and chef in a white chef's jacket in front of bookshelves"></div>
</section>

<nav class="quick">
  <a class="btn" style="left:150px;top:17px;width:157px">Weekend events</a>
  <a class="btn" style="left:400px;top:17px;width:157px">Daily offer</a>
  <a class="btn active" style="left:643px;top:17px;width:159px">Regular menu</a>
  <a class="btn" style="left:899px;top:17px;width:157px">Where to find us</a>
</nav>

<section class="about">
  <h2 class="section-title" style="top:30px">ABOUT US</h2>
  <div class="section-rule" style="top:76px"></div>
  <div class="abs team-photo" role="img" aria-label="The restaurant team in uniforms standing in the dining room"></div>
  <p class="abs about-text">Since 2005, our unique Czech restaurant concept has filled the gap between all the fast food restaurants and expensive so-called luxury restaurants. Our meticulous approach to meat and cooking in general has brought us to the top of Czech gastronomy and has earned us features on several TV shows.</p>
  <a class="btn on-light" style="left:636px;top:243px;width:136px">Video archives</a>
  <a class="btn on-light" style="left:905px;top:243px;width:138px">3D virtual tour</a>
  <a class="btn on-light" style="left:159px;top:387px;width:136px">Restaurant concept</a>
  <a class="btn on-light" style="left:353px;top:387px;width:135px">Our steaks</a>
  <div class="abs interior-photo" role="img" aria-label="Panoramic view of the red dining room interior and bar"></div>
</section>

<section class="menu">
  <h2 class="section-title" style="top:62px">MENU</h2>
  <div class="section-rule" style="top:106px"></div>
  <p class="abs tagline">We make international <em>dishes according to traditional<br>recipes as people all over the world enjoy them.</em></p>
  <p class="abs menu-sub">Our guests get exactly as stated on the menu.</p>
  <p class="abs menu-quote">Give people what they want and what they deserve for their money.<small>– T. Veverka, founder of the Ohnivá Korna concept</small></p>

  <div class="abs card">
    <h3 style="left:26px;top:34px">Weekend special</h3>
    <div class="rule" style="left:26px;top:84px"></div>
    <p class="meta" style="left:26px;top:98px">Including Friday evening,<br><b>November 2–4, 2018</b></p>
    <p class="desc" style="left:26px;top:156px;width:222px">On weekends, we mostly offer dishes made in an oven, grilled and broiled over wood. We make whole large chunks of game, such as 70kg legs of beef and diverse wild game – boar, lamb, fallow deer, mouflon. We roast our dishes at low temperatures for up to 12 hours, making them juicy and beautifully scented with smoke.</p>

    <div class="vline" style="left:265px;top:80px;height:300px"></div>
    <div class="vline" style="left:426px;top:80px;height:300px"></div>
    <div class="vline" style="left:598px;top:80px;height:300px"></div>

    <div class="dish" style="left:272px;top:46px;width:140px">
      <div class="icon"><svg width="50" height="40" viewBox="0 0 50 40"><path d="M4 16h42c0 12-9 20-21 20S4 28 4 16z" fill="none" stroke="#c5161d" stroke-width="3"/><path d="M14 10c2-3-2-5 0-8M25 10c2-3-2-5 0-8M36 10c2-3-2-5 0-8" fill="none" stroke="#c5161d" stroke-width="2.5"/></svg></div>
      <h4>Starter</h4>
      <p>Homemade sirloin<br>steak tartare, 50 g</p>
      <div class="note">Pre-mixed, garlic toast</div>
      <div class="price">CZK 129</div>
    </div>
    <div class="dish" style="left:440px;top:46px;width:144px">
      <div class="icon"><svg width="54" height="40" viewBox="0 0 54 40"><path d="M8 10c10-8 30-8 40 2 6 8 0 20-14 22C16 36 2 30 4 20c1-4 2-7 4-10z" fill="none" stroke="#c5161d" stroke-width="3"/><path d="M16 14l20 12M22 10l18 10M14 22l16 8" stroke="#c5161d" stroke-width="2"/></svg></div>
      <h4>Main Meal</h4>
      <p>Beef sirloin in cream<br>sauce known as<br>"svíčková"</p>
      <div class="note">Matured Uruguayan<br>rump, homemade<br>Carlsbad dumplings,<br>lemon, lingonberries</div>
      <div class="price">CZK 209</div>
    </div>
    <div class="dish" style="left:610px;top:46px;width:150px">
      <div class="icon"><svg width="54" height="40" viewBox="0 0 54 40"><path d="M8 10c10-8 30-8 40 2 6 8 0 20-14 22C16 36 2 30 4 20c1-4 2-7 4-10z" fill="none" stroke="#c5161d" stroke-width="3"/><path d="M16 14l20 12M22 10l18 10M14 22l16 8" stroke="#c5161d" stroke-width="2"/></svg></div>
      <h4>Main Meal</h4>
      <p>Homemade sirloin<br>steak tartare, 150 g</p>
      <div class="note">Pre-mixed, garlic toast</div>
      <div class="price">CZK 289</div>
    </div>

    <h3 style="left:26px;top:432px">Daily Offer</h3>
    <div class="rule" style="left:26px;top:482px"></div>
    <p class="meta" style="left:26px;top:494px"><b>November 15, 2018</b></p>
    <p class="desc" style="left:26px;top:530px;width:212px">We cook a lunch menu every weekday using fresh local ingredients. The offers are varied and diverse and do not repeat for about 2 months.</p>

    <div class="vline" style="left:254px;top:450px;height:236px"></div>
    <div class="vline" style="left:495px;top:450px;height:236px"></div>

    <div class="dish" style="left:297px;top:444px;width:150px">
      <div class="icon"><svg width="50" height="40" viewBox="0 0 50 40"><path d="M4 16h42c0 12-9 20-21 20S4 28 4 16z" fill="none" stroke="#c5161d" stroke-width="3"/><path d="M14 10c2-3-2-5 0-8M25 10c2-3-2-5 0-8M36 10c2-3-2-5 0-8" fill="none" stroke="#c5161d" stroke-width="2.5"/></svg></div>
      <h4>Soup</h4>
      <p style="font-weight:500">Potato soup<br>With forest mushrooms.</p>
      <div class="note">small</div>
      <div class="price">CZK 49</div>
      <div class="note" style="margin-top:0">large</div>
      <div class="price">CZK 55</div>
    </div>
    <div class="dish" style="left:518px;top:444px;width:190px">
      <div class="icon"><svg width="54" height="40" viewBox="0 0 54 40"><path d="M8 10c10-8 30-8 40 2 6 8 0 20-14 22C16 36 2 30 4 20c1-4 2-7 4-10z" fill="none" stroke="#c5161d" stroke-width="3"/><path d="M16 14l20 12M22 10l18 10M14 22l16 8" stroke="#c5161d" stroke-width="2"/></svg></div>
      <h4>Main Meal</h4>
      <p style="font-weight:500">Mushroom veal stew</p>
      <div class="note">Stewed veal in delicate cream<br>sauce with forest mushrooms<br>and homemade bread dumplings</div>
      <div class="price">CZK 179</div>
    </div>
  </div>

  <div class="abs menu-links">
    <a class="btn" style="left:47px;width:156px">Regular Menu</a>
    <a class="btn" style="left:367px;width:157px">Drinks List</a>
    <a class="btn" style="left:684px;width:158px">Wine List</a>
  </div>
</section>

<section class="contact">
  <div class="contact-side" style="left:0;width:383px" role="img" aria-label="Parking area and road beside the restaurant"></div>
  <div class="contact-side" style="left:819px;width:381px" role="img" aria-label="Street view with road signs near the restaurant"></div>
  <div class="abs contact-photo" role="img" aria-label="Exterior of the restaurant building with white parasols on the terrace"></div>
  <h2 class="section-title">CONTACT</h2>
  <div class="section-rule" style="left:571px;top:60px"></div>
  <div class="contact-block" style="right:826px;text-align:right">
    <h5>Ohnivá Korna Restaurant</h5>
    Open daily from 11 am to 10 pm,<br>Fridays and Saturdays until 11 pm<br>Lipová 27,<br>562 14 Dolní Brod (map)<br>restaurant@ohnivakorna.cz<br>+420 600 123 456
  </div>
  <div class="contact-block" style="left:845px">
    <h5>Billing details</h5>
    Tomáš Veverka<br>Lipová 48, 562 14 Dolní Brod<br>Company ID: 48210573,<br>VAT ID: CZ6104283951<br>tomas.veverka@ohnivakorna.cz
  </div>
  <a class="abs map-btn">Where to find us</a>
</section>

<footer class="footer">
  <nav class="abs foot-nav"><span>ABOUT US</span><span>MENU</span><span>CONTACT</span></nav>
  <p class="abs foot-book">Bookings are accepted only by telephone at <b>+420 600 123 456</b>.</p>
  <div class="abs social">
    <div class="cur"><i></i>Friendbook</div>
    <div><i></i>Circles</div>
    <div><i></i>TravelNotes</div>
    <div><i></i>Placemap</div>
  </div>
  <div class="abs foot-meta"><span>On service: Klidné weby</span><span>© 2017–2019 WebForge</span><span>Latest changes: January 25, 2019</span></div>
</footer>

</body>
</html>
```